Brantley Energy PowerPoint Design

Looking for a sleek PowerPoint design for our energy services company. We supply EV charging, Solar, Battery Storage and more.

Please make the background white with hints of gray and utilize the exact dark blue and light blue colors in the logo.

This design should be sharp with minimal round edges.

Colors

Designer to choose colors to be used in the design.

```html
<!DOCTYPE html>
<html lang="en">
<head>
<meta charset="UTF-8">
<title>The Story Of Us</title>
<link rel="stylesheet" href="https://fonts.googleapis.com/css2?family=Montserrat:wght@400;600;700&display=swap">
<style>
  :root {
    --light-blue: #3aa6e8;
    --dark-blue: #0b2c5f;
    --mid-blue: #1f67a8;
    --ink: #333333;
    --white: #ffffff;
    --hint-gray: #f4f5f7;
  }
  * { margin: 0; padding: 0; box-sizing: border-box; }
  html, body { width: 1200px; height: 675px; overflow: hidden; background: var(--white); }
  .slide {
    position: relative; width: 1200px; height: 675px; overflow: hidden;
    background: linear-gradient(to bottom, var(--white) 0%, var(--white) 55%, var(--hint-gray) 70%);
    font-family: 'Montserrat', sans-serif;
  }
  .accent-bar { position: absolute; left: 26px; top: 25px; width: 5px; height: 92px; background: var(--dark-blue); }
  .accent-bar::before { content: ""; position: absolute; left: 0; top: 0; width: 5px; height: 20px; background: var(--light-blue); }
  .bottom-band {
    position: absolute; left: 0; top: 478px; width: 1200px; height: 197px;
    background: linear-gradient(to bottom, var(--light-blue) 0%, var(--mid-blue) 50%, var(--dark-blue) 100%);
  }
  .eyebrow {
    position: absolute; top: 87px; width: 100%; text-align: center;
    font-size: 12px; font-weight: 600; letter-spacing: 3.6px; color: var(--light-blue);
  }
  .title {
    position: absolute; top: 110px; width: 100%; text-align: center;
    font-size: 57px; font-weight: 700; letter-spacing: -0.5px; line-height: 1.1;
  }
  .title .warm { color: var(--light-blue); }
  .title .cool { color: var(--dark-blue); }
  .column { position: absolute; top: 213px; width: 260px; text-align: center; }
  .column h3 { font-size: 13px; font-weight: 700; letter-spacing: 3.4px; color: var(--dark-blue); margin-bottom: 8px; }
  .column p { font-size: 10.5px; line-height: 20px; color: var(--ink); }
  .col-1 { left: 81px; } .col-2 { left: 462px; } .col-3 { left: 850px; }
  .card {
    position: absolute; top: 299px; width: 342px; height: 342px; background: var(--white);
    box-shadow: 0 1px 6px rgba(0,0,0,0.12); padding: 15px;
  }
  .card-1 { left: 41px; } .card-2 { left: 429px; } .card-3 { left: 812px; }
  .photo { width: 100%; height: 100%; }
  .photo-sunflower { background: linear-gradient(135deg, #3f86d6 0%, #9cc8ef 45%, #f2c230 75%, #5f8f3a 100%); }
  .photo-blocks { background: radial-gradient(circle at 55% 50%, #5fae2e 0%, #8cc16a 35%, #e6ebe6 70%); }
  .photo-solar { background: linear-gradient(160deg, #d9d9d6 0%, #1e3a7a 30%, #8fc7ee 60%, #6cb33a 100%); }
</style>
</head>
<body>
<div class="slide">
  <div class="bottom-band"></div>
  <div class="accent-bar"></div>

  <div class="eyebrow">KEEP IT SIMPLE</div>
  <h1 class="title"><span class="warm">The Story</span> <span class="cool">Of Us</span></h1>

  <div class="column col-1">
    <h3>SAMPLE TEXT</h3>
    <p>Lorem ipsum dolor sit amet, errem<br>malorum in nec, ne sit esse solet</p>
  </div>
  <div class="column col-2">
    <h3>SAMPLE TEXT</h3>
    <p>Lorem ipsum dolor sit amet, errem<br>malorum in nec, ne sit esse solet</p>
  </div>
  <div class="column col-3">
    <h3>SAMPLE TEXT</h3>
    <p>Lorem ipsum dolor sit amet, errem<br>malorum in nec, ne sit esse solet</p>
  </div>

  <div class="card card-1">
    <div class="photo photo-sunflower" role="img" aria-label="Sunflower in front of a glass building reflecting blue sky with large yellow energy lettering"></div>
  </div>
  <div class="card card-2">
    <div class="photo photo-blocks" role="img" aria-label="Green letter cubes arranged crossword style spelling green energy"></div>
  </div>
  <div class="card card-3">
    <div class="photo photo-solar" role="img" aria-label="Solar panel above a blue puzzle house shape showing sky and grass, on a wooden background"></div>
  </div>
</div>
</body>
</html>
```